Webdesign für Full-Service-Internetagentur
Zielgruppe
Brenntaler Webdesign – Ihr Partner für außergewöhnliche Onlinepräsenzen
Wir bieten seit mehr als 16 Jahren Internetauftritte für kleine und mittelständische Unternehmen an.
Als Full-Service-Internetagentur liefern wir Ihnen individuelle auf Ihre Bedürfnisse, Ihre Branche und Ihre Zielgruppe zugeschnittene Lösungen für Ihre Onlinepräsentation an. Unser Angebot beinhaltet sowohl ein ideenreiches Webdesign kombiniert mit den aktuellsten Grundsätzen für Web-Programmierung als auch die Unterstützung für Ihr erfolgreiches Werben im Internet.
Eine gute Beratung heißt für uns genau hinhören und verstehen, was Sie wirklich brauchen. Je besser wir Ihre Ziele kennen, desto besser können wir Ihre Onlinepräsenz umsetzen. Unsere Kundenberater erläutern Ihnen persönlich mit Enthusiasmus die verschiedenen Möglichkeiten der Darstellung Ihrer Firma im Internet und entwickeln Konzepte, die Ihren Anforderungen bestmöglich entsprechen. Nicht nur während der Projektphase, sondern auch nach Onlinestellung Ihrer Internetseite stehen wir Ihnen mit persönlicher Kundenbetreuung und Supportdienstleistungen zur Verfügung.
Aufgabenstellung
siehe : https://www.brenntaler-webdesign.de/

```html
<!DOCTYPE html>
<html lang="de">
<head>
<meta charset="utf-8">
<title>Brenntaler Webdesign – Ihr Partner</title>
<link rel="stylesheet" href="https://fonts.googleapis.com/css2?family=Montserrat:wght@300;400;500;600&display=swap">
<style>
:root{
  --red:#e30613;
  --ink:#1f1f1f;
  --text:#7a7a7a;
  --muted:#a5a5a5;
  --line:#e2e2e2;
  --tag:#eeeeee;
  --band:#f6f7f9;
  --foot:#d9d9d9;
  --foot-dark:#8e8e8e;
}
*{box-sizing:border-box;margin:0;padding:0}
html,body{width:1200px;height:3769px;overflow:hidden}
body{position:relative;font-family:"Montserrat",Arial,sans-serif;color:var(--ink);background:#fff}
a{text-decoration:none}
.abs{position:absolute}
.center{left:0;width:1200px;text-align:center}
.eyebrow{font-size:9px;font-weight:500;color:var(--red);letter-spacing:.5px;text-transform:uppercase}
.h2{font-size:24px;font-weight:400;letter-spacing:.3px}
.lead{font-size:11.5px;line-height:19px;color:var(--text)}
.btn{display:flex;align-items:center;justify-content:center;height:30px;border-radius:15px;background:var(--red);color:#fff;font-size:10px;font-weight:600;letter-spacing:.5px;text-transform:uppercase}
.btn-outline{background:transparent;border:1px solid var(--red);color:var(--red)}

/* header + hero */
.hero{top:0;left:0;width:1200px;height:600px;background:radial-gradient(ellipse at 70% 10%,#fafafa 0%,#eeeeee 55%,#e4e4e4 100%)}
.brand{left:92px;top:11px;font-size:19px;font-weight:400;color:var(--ink)}
.nav{top:19px;left:0;width:1200px;font-size:11px;font-weight:500}
.nav span{position:absolute}
.nav-cta{left:956px;top:10px;width:149px}
.hero-title{top:252px;font-size:30px;font-weight:300;letter-spacing:.3px}
.hero-sub{top:308px;font-size:14px;line-height:23px;color:#6a6a6a;font-weight:300}

/* offer */
.service{width:165px}
.service-icon{width:32px;height:32px}
.service-title{margin-top:14px;font-size:10.5px;font-weight:500;line-height:18px;text-transform:uppercase;letter-spacing:.3px}
.service-text{margin-top:8px;font-size:10.5px;line-height:18px;color:var(--text)}
.more{margin-top:12px;font-size:9px;font-weight:500;color:var(--red);text-transform:uppercase}

/* about */
.about{top:1105px;left:0;width:1200px;height:418px;background:var(--band)}
.about-h{font-size:22px;font-weight:400}
.monitor{left:642px;top:1193px;width:314px;height:263px}

/* references */
.ref{width:226px}
.ref-img{width:226px;height:188px}
.ref-title{margin-top:20px;font-size:10.5px;font-weight:500;line-height:16px;text-transform:uppercase;letter-spacing:.3px}
.tags{margin-top:8px;display:flex;gap:8px}
.tag{height:20px;padding:0 16px;border-radius:10px;background:var(--tag);font-size:7.5px;color:#888;display:flex;align-items:center;text-transform:uppercase;letter-spacing:.3px}

/* customers */
.logos{top:2471px;left:243px;width:713px;display:flex;justify-content:space-between;align-items:center}
.client{display:flex;align-items:center;gap:6px;font-size:14px;font-weight:600;color:#b9b9b9}
.client i{display:block;width:16px;height:16px;background:#d2d2d2}
.divider{top:2560px;left:243px;width:713px;height:1px;background:var(--line)}

/* blog */
.post{width:226px}
.post-img{width:226px;height:143px}
.post-title{margin-top:22px;font-size:12px;font-weight:500;line-height:19px;color:var(--red)}
.post-text{margin-top:8px;font-size:10.5px;line-height:18px;color:var(--text)}
.post-date{margin-top:14px;font-size:7px;color:var(--muted)}

/* contact */
.field{font-size:9px;color:var(--muted);border-bottom:1px solid var(--line);height:22px}

/* footer */
.footer{top:3685px;left:0;width:1200px;height:61px;background:var(--foot)}
.social{top:3711px;left:552px;display:flex;gap:22px}
.social span{display:block;width:13px;height:13px;border-radius:50%;background:#222}
.copy{top:3746px;left:0;width:1200px;height:23px;background:var(--foot-dark);color:#eee;font-size:8px;display:flex;align-items:center;justify-content:center}
</style>
</head>
<body>

<section class="abs hero" role="img" aria-label="Heller Schreibtisch mit Tastatur, Maus und Ohrhörern"></section>
<header>
  <div class="abs brand">Brenntaler Webdesign</div>
  <nav class="abs nav">
    <span style="left:415px">Agentur</span>
    <span style="left:502px">Referenzen</span>
    <span style="left:607px">Engagement</span>
    <span style="left:721px">Aktuelles</span>
    <span style="left:815px">Kontakt</span>
    <span style="left:901px">FAQ</span>
  </nav>
  <a class="abs btn nav-cta">Angebot einholen</a>
</header>
<h1 class="abs center hero-title">Brenntaler Webdesign – Ihr Partner</h1>
<p class="abs center hero-sub">Wir bieten seit mehr als 16 Jahren Internetauftritte für kleine<br>und mittelständische Unternehmen an</p>
<a class="abs btn btn-outline" style="left:470px;top:373px;width:118px">Leistungen</a>
<a class="abs btn" style="left:609px;top:373px;width:149px">Projekt starten</a>

<!-- Angebot -->
<p class="abs center eyebrow" style="top:667px">Unser Angebot</p>
<h2 class="abs center h2" style="top:694px">Für außergewöhnliche Onlinepräsenzen</h2>
<p class="abs center lead" style="top:740px">Als Full-Service-Internetagentur liefern wir Ihnen individuelle auf Ihre Bedürfnisse, Ihre<br>Branche und Ihre Zielgruppe zugeschnittene Lösungen für Ihre Onlinepräsentation an.</p>

<div class="abs service" style="left:243px;top:822px">
  <svg class="service-icon" viewBox="0 0 32 32" fill="none" stroke="var(--red)" stroke-width="1.4"><rect x="4" y="4" width="24" height="20" rx="2"/><circle cx="16" cy="14" r="5"/><path d="M16 11v6M14 13h4M10 28h12"/></svg>
  <div class="service-title">Konzeption &amp; Beratung</div>
  <div class="service-text">Wir entwickeln Ihr individu-<br>elles Konzept und begleiten<br>Sie über die Fertigstellung<br>hinaus.</div>
  <div class="more">Mehr erfahren</div>
</div>
<div class="abs service" style="left:426px;top:822px">
  <svg class="service-icon" viewBox="0 0 32 32" fill="none" stroke="var(--red)" stroke-width="1.4"><rect x="3" y="4" width="26" height="19" rx="1"/><path d="M3 8h26M12 23v5M20 23v5M9 28h14M12 17l4-5 4 5"/></svg>
  <div class="service-title">Webdesign &amp;<br>Programmierung</div>
  <div class="service-text">Wir setzen Ihre individuell<br>gestaltete Webseite mittels<br>aktueller Web-Technologien<br>um.</div>
  <div class="more">Mehr erfahren</div>
</div>
<div class="abs service" style="left:609px;top:822px">
  <svg class="service-icon" viewBox="0 0 32 32" fill="none" stroke="var(--red)" stroke-width="1.4"><rect x="12" y="3" width="16" height="12" rx="1"/><path d="M4 16l8-3v12l-8-3zM12 15l6 4M6 22l2 6"/><path d="M17 8l3 2 4-4"/></svg>
  <div class="service-title">SEO &amp; Online Marketing</div>
  <div class="service-text">Wir analysieren Ihre Web-<br>seite und schaffen Voraus-<br>setzungen für ein optimales<br>Such-Ranking.</div>
  <div class="more">Mehr erfahren</div>
</div>
<div class="abs service" style="left:792px;top:822px">
  <svg class="service-icon" viewBox="0 0 32 32" fill="none" stroke="var(--red)" stroke-width="1.4"><path d="M9 14a6 6 0 0 1 11-4 5 5 0 0 1 7 5 4 4 0 0 1-2 7H8a4 4 0 0 1 1-8z"/><rect x="10" y="18" width="12" height="10" rx="1"/><path d="M13 22h6M13 25h6"/></svg>
  <div class="service-title">Domain &amp; Webhosting</div>
  <div class="service-text">Alles was Sie für Ihr Webpro-<br>jekt brauchen.</div>
  <div class="more">Mehr erfahren</div>
</div>

<!-- Über uns -->
<section class="abs about"></section>
<p class="abs eyebrow" style="left:243px;top:1196px">Über uns</p>
<h2 class="abs about-h" style="left:243px;top:1226px">Lorem ipsum dollor</h2>
<p class="abs lead" style="left:243px;top:1271px;width:360px;font-size:10.5px;line-height:18.5px">Lorem ipsum dolor sit amet, consectetur adipiscing elit. Fusce<br>nisi enim, vulputate at justo tristique, tempor sagittis dolor.<br>Cum sociis natoque penatibus et magnis dis parturient<br>montes, nascetur ridiculus mus. Donec sit amet ligula conse-<br>quat urna posuere convallis.</p>
<a class="abs btn" style="left:243px;top:1400px;width:150px">Mehr erfahren</a>
<div class="abs monitor" role="img" aria-label="Bildschirm mit Vorschau der Agentur-Webseite" style="background:linear-gradient(180deg,#2a2a2a 0%,#2a2a2a 72%,#d8d8d8 72%,#c9c9c9 84%,transparent 84%);border-radius:6px"></div>

<!-- Referenzen -->
<p class="abs center eyebrow" style="top:1584px">Latest Design</p>
<h2 class="abs center h2" style="top:1612px">Referenzen</h2>

<div class="abs ref" style="left:243px;top:1684px">
  <div class="ref-img" role="img" aria-label="Roter Lastwagen eines Bauunternehmens" style="background:linear-gradient(160deg,#5a7a4a,#a8342c 55%,#3c3a36)"></div>
  <div class="ref-title">Varnek Bauunternehmen</div>
  <div class="tags"><span class="tag">SEO</span><span class="tag">Domain</span></div>
</div>
<div class="abs ref" style="left:487px;top:1684px">
  <div class="ref-img" role="img" aria-label="Modernes Haus mit Pool" style="background:linear-gradient(170deg,#4f86c4 0%,#a9c7e3 40%,#e9ebea 60%,#5f8a4a 100%)"></div>
  <div class="ref-title">Lindner &amp; Haas GmbH<br>Werkzeug- und Maschinenbau</div>
  <div class="tags"><span class="tag">SEO</span><span class="tag">Webdesign</span></div>
</div>
<div class="abs ref" style="left:730px;top:1684px">
  <div class="ref-img" role="img" aria-label="Gebäudefassade mit roter Markise" style="background:linear-gradient(180deg,#8d8b88,#c63a26 45%,#b9b6b0 70%,#5d5a55)"></div>
  <div class="ref-title">Marlene´s Pflegedienst</div>
  <div class="tags"><span class="tag">SEO</span><span class="tag">Webdesign</span></div>
</div>

<div class="abs ref" style="left:243px;top:1977px">
  <div class="ref-img" role="img" aria-label="Sportlerin beim Dehnen im Wald" style="background:linear-gradient(160deg,#e3a54a,#b78546 50%,#6b4a2c)"></div>
  <div class="ref-title">Helfende Hand Ines Berger</div>
  <div class="tags"><span class="tag">Konzept</span><span class="tag">Domain</span></div>
</div>
<div class="abs ref" style="left:487px;top:1977px">
  <div class="ref-img" role="img" aria-label="Helles Badezimmer mit Badewanne" style="background:linear-gradient(170deg,#6f6f6f,#c6c6c6 45%,#eeeeee 80%,#d4d4d4)"></div>
  <div class="ref-title">Sanitär-Heizung-Klima Dorfmann</div>
  <div class="tags"><span class="tag">SEO</span><span class="tag">Webdesign</span></div>
</div>
<div class="abs ref" style="left:730px;top:1977px">
  <div class="ref-img" role="img" aria-label="Dunkle Industriehalle" style="background:linear-gradient(160deg,#1f2326,#36424a 55%,#181b1e)"></div>
  <div class="ref-title">Prozesstechnik Rehberg GmbH</div>
  <div class="tags"><span class="tag">SEO</span><span class="tag">Webdesign</span></div>
</div>

<a class="abs btn" style="left:524px;top:2278px;width:150px">Alle Projekte</a>

<!-- Kunden -->
<p class="abs center eyebrow" style="top:2363px">Happy Customers</p>
<h2 class="abs center h2" style="top:2389px">Unsere zufriedenen Kunden</h2>
<div class="abs logos">
  <span class="client"><i></i>Kalm</span>
  <span class="client">Orvin</span>
  <span class="client"><i></i>Seelig</span>
  <span class="client">Tessa</span>
  <span class="client">Hollweg</span>
  <span class="client"><i></i>Brisa</span>
</div>
<div class="abs divider"></div>

<!-- Blog -->
<p class="abs center eyebrow" style="top:2622px">Blog</p>
<h2 class="abs center h2" style="top:2648px">Was es neues gibt</h2>

<div class="abs post" style="left:243px;top:2722px">
  <div class="post-img" role="img" aria-label="Team arbeitet an Laptops" style="background:linear-gradient(160deg,#4a4540,#8b7d6d 50%,#2f2c29)"></div>
  <div class="post-title">"Für jeden" ETWAS bei Brenntaler<br>Webdesign</div>
  <div class="post-text">Wir entwickeln Ihr individuelles Konzept<br>und begleiten Sie über die Fertigstel-<br>lung hinaus.</div>
  <div class="post-date">10 May 2019</div>
</div>
<div class="abs post" style="left:487px;top:2722px">
  <div class="post-img" role="img" aria-label="Laptop und Tasse auf hellem Tisch" style="background:linear-gradient(170deg,#f1f1f1,#d9d9d9 55%,#8d9095)"></div>
  <div class="post-title">"Für jeden" ETWAS bei Brenntaler<br>Webdesign</div>
  <div class="post-text">Wir entwickeln Ihr individuelles Konzept<br>und begleiten Sie über die Fertigstel-<br>lung hinaus.</div>
  <div class="post-date">10 May 2019</div>
</div>
<div class="abs post" style="left:730px;top:2722px">
  <div class="post-img" role="img" aria-label="Person mit Kopfhörern am Laptop" style="background:linear-gradient(160deg,#2c3f52,#4d6277 50%,#9aa4ad)"></div>
  <div class="post-title">"Für jeden" ETWAS bei Brenntaler<br>Webdesign</div>
  <div class="post-text">Wir entwickeln Ihr individuelles Konzept<br>und begleiten Sie über die Fertigstel-<br>lung hinaus.</div>
  <div class="post-date">10 May 2019</div>
</div>

<a class="abs btn" style="left:524px;top:3058px;width:150px">Alle Artikle</a>

<!-- Kontakt -->
<p class="abs center eyebrow" style="top:3150px">In Kontakt kommen</p>
<h2 class="abs center h2" style="top:3177px">Wir haben Ihr Interesse geweckt?</h2>
<p class="abs center lead" style="top:3249px;font-size:11px">Guter Rat bedeutet, aufmerksam zuzuhören und zu verstehen, was Sie wirklich<br>brauchen. Je besser wir Ihre Ziele kennen, desto besser können wir Ihre Online-Präsenz<br>realisieren</p>
<form>
  <div class="abs field" style="left:364px;top:3337px;width:226px">Name</div>
  <div class="abs field" style="left:609px;top:3337px;width:224px">Email</div>
  <div class="abs field" style="left:364px;top:3380px;width:226px">Telefon</div>
  <div class="abs field" style="left:609px;top:3380px;width:224px">Website</div>
  <div class="abs field" style="left:364px;top:3422px;width:469px;height:100px">Nachricht</div>
  <a class="abs btn" style="left:505px;top:3562px;width:188px">Formular abschicken</a>
</form>

<!-- Footer -->
<footer>
  <div class="abs footer"></div>
  <div class="abs social" aria-label="Soziale Netzwerke"><span></span><span></span><span></span></div>
  <div class="abs copy">© 2019 by Brenntaler Webdesign</div>
</footer>

</body>
</html>
```